Redesign Digital Lending Mobile App - Android/ Flutter

Want to re-theme an existing Digital Lending Mobile app to simplify customer journeys, as well as uplift the UI.

Most users will have small screen phones so the design needs to take that into consideration while also adapting to those with larger devices, like admins with Tablets.

Have already laid out customer journeys on Figma with guidance on how the flow of the app should be. https://www.plavorix.example/design/q4tRbW8mZkLs2HdYc7NpXa/LoqTab?node-id=5-2914&t=Vb3kQmXz8RtYpLwN-2

Video capture of current app: https://files.tremodex.example/file/d/7Hq2WzLmRtPxYvBn4KcDsJfGaUeNo9MiQ/view
https://files.tremodex.example/file/d/3Zp8VnKxQwLyTcRm6BgHsDfJaEuPo2WiT/view

The documented views for Web are also here https://docs.quarvelin.example/edit?id=4B2C8D03AF71E95D!skx82b1047c3e5d40a8f2c7d9b1e4a3f608&resid=4B2C8D03AF71E95D!skx82b1047c3e5d40a8f2c7d9b1e4a3f608&cid=4b2c8d03af71e95d&ithint=file%2Cdocx&redeem=bXZ0cHM6Ly9xdWFydmVsaW4uZXhhbXBsZS93L2MvNGIyYzhkMDNhZjcxZTk1ZC9GWExrUW1QZFJ0V3NZdkJuSGNKeEthWnBMcU5zVGdWbU55UnM3YlF6eDBtN1dkcFpH&migratedtospo=true&wdo=2

Target Market(s)

Kenya, Tanzania, Uganda - Africa

Industry/Entity Type

Fintech

Requirements
Must have
• Responsive for diff screens, esp. in context of smaller screen smartphone
Nice to have
• Thematic components to ensure new views can easily be adapted to these themse

```html
<!DOCTYPE html>
<html lang="en">
<head>
<meta charset="utf-8">
<title>LoqTab — Old vs New Design</title>
<link href="https://fonts.googleapis.com/css2?family=Poppins:wght@400;500;600&display=swap" rel="stylesheet">
<style>
:root{
  --ink:#1b1b1b;--muted:#666;--line:#d6d6d6;--chip:#dcdcdc;--soft:#ececec;
  --navy:#1f4e8c;--green:#3d9a55;--mist:#c9d8e4;--frame:#1f1f1f;
}
*{box-sizing:border-box;margin:0;padding:0}
html,body{width:971px;height:1200px;overflow:hidden;background:#fff}
body{position:relative;font-family:"Poppins",sans-serif;color:var(--ink)}
.section-title{position:absolute;left:0;width:971px;text-align:center;font-size:23px;font-weight:500}
.scr{position:absolute;width:107px;height:211px;border:2px solid var(--frame);border-radius:15px;background:#fff;padding:17px 7px 6px;overflow:hidden;display:flex;flex-direction:column;gap:3px;font-size:4px}
.scr.dim{background:var(--mist)}
.hd{display:flex;align-items:center;justify-content:space-between;font-size:5.5px;font-weight:500;margin-bottom:3px;white-space:nowrap}
.hd .m{margin-right:3px}
.exit{width:7px;height:7px;flex-shrink:0}
.ttl{text-align:center;font-size:5.5px;font-weight:600}
.avatar{width:30px;height:30px;border-radius:50%;background:radial-gradient(circle at 50% 40%,#c9a78b,#3b4f72);margin:2px auto;flex-shrink:0}
.fld{height:11px;border:1px solid var(--line);border-radius:2px;padding:0 3px;display:flex;align-items:center;justify-content:space-between;color:#555;font-size:3.4px;flex-shrink:0}
.sel{height:11px;background:var(--chip);border-radius:2px;padding:0 3px;display:flex;align-items:center;justify-content:space-between;font-size:3.6px;flex-shrink:0;white-space:nowrap}
.sel b{font-weight:600}
.sel .cv{width:5px;height:5px;border-radius:50%;border:0.6px solid #888;font-size:3px;display:flex;align-items:center;justify-content:center;font-style:normal}
.btn{height:10px;border-radius:6px;background:var(--navy);color:#fff;font-size:4.4px;font-weight:500;display:flex;align-items:center;justify-content:center;flex-shrink:0;white-space:nowrap}
.btn.sm{font-size:3.8px;padding:0 5px;height:8px}
.brand{color:var(--ink);font-size:11px;font-weight:600;text-align:center}
.dots{display:flex;gap:4px;justify-content:center;margin:4px 0}
.dots i{width:5px;height:5px;border:0.7px solid #999;border-radius:50%}
.pad{display:grid;grid-template-columns:repeat(3,17px);gap:3px 5px;justify-content:center}
.pad span{width:17px;height:17px;border:1.3px solid #4fae6a;border-radius:50%;display:flex;align-items:center;justify-content:center;font-size:9px;color:#3d9a55}
.del{width:7px;height:4.5px;background:#222;border-radius:1px;justify-self:center;align-self:center}
.note{text-align:center;font-size:4px;color:#444}
.row{display:flex;align-items:center;justify-content:space-between;white-space:nowrap}
.funnel{width:11px;height:11px;border-radius:50%;background:var(--green);display:flex;align-items:center;justify-content:center}
.tabs{display:flex;gap:6px;align-items:center;font-size:4px;white-space:nowrap}
.tab{background:var(--navy);color:#fff;border-radius:5px;padding:2px 5px}
.card{border-radius:2px;padding:4px 4px;display:flex;flex-direction:column;gap:4px;font-size:4px;white-space:nowrap}
.card.g{background:var(--green);color:#fff}
.card.n{background:var(--soft)}
.tiles{display:grid;grid-template-columns:1fr 1fr;gap:2px}
.tile{border-radius:2px;padding:3px 1px;text-align:center;font-size:3.1px;line-height:1.4}
.tile.g{background:var(--green);color:#fff}
.tile.n{background:var(--soft)}
.li{background:var(--chip);border-radius:2px;padding:2px 3px;font-size:3.2px;line-height:1.3;display:flex;justify-content:space-between;align-items:center;flex-shrink:0;white-space:nowrap}
.li b{font-weight:600}
.ring{width:5px;height:5px;border:0.6px solid #555;border-radius:50%;flex-shrink:0}
.search{background:var(--navy);color:#fff;border-radius:6px;height:11px;padding:0 5px;display:flex;align-items:center;justify-content:space-between;font-size:4px;margin-bottom:3px;flex-shrink:0}
.cl{height:15px}
.nav{margin-top:auto;display:flex;justify-content:space-around;align-items:center;border-top:1px solid var(--line);padding-top:3px}
.nav i{width:6px;height:6px;background:#9a9a9a;border-radius:1px}
.nav i.on{width:10px;height:10px;border-radius:50%;background:var(--green)}
.name{text-align:center;font-size:5px;font-weight:500}
.info{border:1px solid var(--soft);border-radius:2px;padding:4px 3px;display:flex;flex-direction:column;gap:7px;font-size:3.2px;white-space:nowrap}
.info div{display:flex;justify-content:space-between}
.info b{font-weight:600}
.menu{position:absolute;left:28px;top:36px;width:70px;background:#fff;padding:3px 6px;display:flex;flex-direction:column;gap:4.5px;font-size:5px;white-space:nowrap}
.ghost{opacity:.45}
.chk{display:flex;align-items:center;gap:3px;font-size:4.4px;white-space:nowrap}
.chk i{width:5px;height:5px;border:0.7px solid #777;border-radius:1px;flex-shrink:0}
.strip{background:var(--green);color:#fff;font-size:3px;padding:2px 3px;display:flex;justify-content:space-between}
.kv{display:flex;justify-content:space-between;font-size:3px;line-height:1.5}
table{width:100%;border-collapse:collapse;font-size:3px;text-align:center}
td{padding:1.8px 0}
.t-g thead td{background:var(--green);color:#fff}
.t-g tr.hl td{background:var(--green);color:#fff}
.t-g tbody{background:#f1f1f1}
.t-n thead td{background:var(--navy);color:#fff}
.t-n tr.hl td{background:#a7cfb6}
.t-n tbody{background:#eef2f5}
.split{display:flex;gap:2px;align-items:center}
.split .sel{flex:1}
.unit{font-size:3px;width:18px;white-space:nowrap}
</style>
</head>
<body>

<h1 class="section-title" style="top:26px">Old Design</h1>
<h1 class="section-title" style="top:607px">New Design</h1>

<!-- ===== OLD ROW 1 ===== -->
<section class="scr" style="left:35px;top:92px">
  <div class="hd"><span><span class="m">≡</span>Client</span><svg class="exit" viewBox="0 0 10 10"><path d="M1 1h5v8H1zM6 5h3.5M8 3.5l1.5 1.5L8 6.5" fill="none" stroke="#333"/></svg></div>
  <div class="ttl">Create Client</div>
  <div class="avatar" role="img" aria-label="Client profile photo"></div>
  <div class="fld">First Name</div><div class="fld">Middle Name</div><div class="fld">Mobile Number</div><div class="fld">National ID</div><div class="fld">Gender</div><div class="fld">Date of Birth</div>
</section>

<section class="scr" style="left:162px;top:92px;padding-top:36px">
  <div class="brand">LoqTab</div>
  <div class="dots"><i></i><i></i><i></i><i></i><i></i><i></i></div>
  <div class="pad"><span>1</span><span>2</span><span>3</span><span>4</span><span>5</span><span>6</span><span>7</span><span>8</span><span>9</span><i></i><span>0</span><i class="del"></i></div>
  <div class="note" style="margin-top:6px">Forget Passcode Login Manually</div>
</section>

<section class="scr" style="left:290px;top:92px">
  <div class="hd"><span><span class="m">≡</span>Loan Book</span><svg class="exit" viewBox="0 0 10 10"><path d="M1 1h5v8H1zM6 5h3.5M8 3.5l1.5 1.5L8 6.5" fill="none" stroke="#333"/></svg></div>
  <div class="row" style="font-size:5px">Filter<span class="funnel"><svg width="6" height="6" viewBox="0 0 10 10"><path d="M1 1h8L6 5v4L4 8V5z" fill="none" stroke="#fff"/></svg></span></div>
  <div class="tabs" style="margin:4px 0"><span class="tab">Loan Summary</span><span>Loan Listing</span></div>
  <div class="card g"><div class="row"><span>Name:</span><span>Amani Kiprono</span></div><div class="row"><span>Mobile No:</span><span>7200001234</span></div><div class="row"><span>Outstanding Balance:</span><span>90000.0</span></div><div>Last Repayment Date: 2024-07-08</div><div>Next Repayment Date: 2024-08-08</div></div>
</section>

<section class="scr" style="left:416px;top:92px">
  <div class="hd"><span><span class="m">≡</span>Loan Book</span><svg class="exit" viewBox="0 0 10 10"><path d="M1 1h5v8H1zM6 5h3.5M8 3.5l1.5 1.5L8 6.5" fill="none" stroke="#333"/></svg></div>
  <div class="row" style="font-size:5px">Filter<span class="funnel"><svg width="6" height="6" viewBox="0 0 10 10"><path d="M1 1h8L6 5v4L4 8V5z" fill="none" stroke="#fff"/></svg></span></div>
  <div class="tabs"><span class="tab">Loan Summary</span><span>Loan Listing</span></div>
  <div class="tiles"><div class="tile g">0<br>Total Active Clients</div><div class="tile g">0<br>Total New Clients</div><div class="tile g">30012.00 to 3 Clients<br>Total Disbursed</div><div class="tile g">5502.00 from 3 Clients<br>Total Collected</div><div class="tile g">0.00 from 0 Clients<br>Total Missed</div></div>
  <div class="li" style="margin-top:4px"><span>Total Active<br><b>0.00 for 0 Clients</b></span><i class="ring"></i></div>
  <div class="li"><span>Total Near Due<br><b>20516.53 from 3 Clients</b></span><i class="ring"></i></div>
  <div class="li"><span>Total Due<br><b>0.00 from 0 Clients</b></span><i class="ring"></i></div>
  <div class="li"><span>Total Overdue<br><b>0.00 for 0 Clients</b></span><i class="ring"></i></div>
</section>

<section class="scr" style="left:542px;top:92px">
  <div class="hd"><span><span class="m">≡</span>Clients</span><svg class="exit" viewBox="0 0 10 10"><path d="M1 1h5v8H1zM6 5h3.5M8 3.5l1.5 1.5L8 6.5" fill="none" stroke="#333"/></svg></div>
  <div class="search">Search here<span>⌕</span></div>
  <div class="li cl"><span>Baraka Odhiambo<br><b>000000001</b></span><i class="ring"></i></div>
  <div class="li cl"><span>Jabali Mwende<br><b>000000002</b></span><i class="ring"></i></div>
  <div class="li cl"><span>Amani Kiprono<br><b>000000003</b></span><i class="ring"></i></div>
  <div class="li cl"><span>Zawadi Njeri<br><b>000000004</b></span><i class="ring"></i></div>
  <div class="li cl"><span>Tumaini Achieng<br><b>000000005</b></span><i class="ring"></i></div>
  <div class="li cl"><span>Faraji Oloo Wekesa<br><b>000000006</b></span><i class="ring"></i></div>
  <div class="li cl"><span>Amani Kiprono<br><b>000000007</b></span><i class="ring"></i></div>
</section>

<section class="scr" style="left:669px;top:92px">
  <div class="hd"><span><span class="m">≡</span>Client</span><svg class="exit" viewBox="0 0 10 10"><path d="M1 1h5v8H1zM6 5h3.5M8 3.5l1.5 1.5L8 6.5" fill="none" stroke="#333"/></svg></div>
  <div class="brand" style="margin-top:10px">LoqTab</div>
  <div class="ttl" style="margin:3px 0 22px">Please enter your<br>credentials</div>
  <div class="fld">Tenant<span>▦</span></div><div class="fld">Username<span>●</span></div><div class="fld">Password<span>◉</span></div>
  <div class="btn" style="margin-top:4px">Login</div>
</section>

<section class="scr" style="left:795px;top:92px">
  <div class="hd"><span><span class="m">≡</span>Loan Book</span><svg class="exit" viewBox="0 0 10 10"><path d="M1 1h5v8H1zM6 5h3.5M8 3.5l1.5 1.5L8 6.5" fill="none" stroke="#333"/></svg></div>
  <div class="row" style="font-size:5.5px;font-weight:500;margin-bottom:6px">Filters<span class="funnel" style="color:#fff;font-size:6px">×</span></div>
  <div class="sel" style="height:13px"><span>Loan Status<br><b>Select Loan Status</b></span><i class="cv">⌄</i></div>
  <div class="sel" style="height:13px"><span>Office<br><b>Select Offices</b></span><i class="cv">⌄</i></div>
  <div class="sel" style="height:13px"><span>Loan Officers<br><b>No Loan Officers Found</b></span><i class="cv">⌄</i></div>
  <div class="sel" style="height:13px"><span>Loan Products<br><b>Select Loan Products</b></span><i class="cv">⌄</i></div>
  <div class="sel" style="height:13px"><span>Funds<br><b>Select Funds</b></span><i class="cv">⌄</i></div>
  <div class="row" style="justify-content:center;gap:4px;margin-top:3px"><span class="btn sm">Apply filters</span><span class="btn sm">Clear filters</span></div>
  <div class="nav"><i class="on"></i><i></i><i></i><i></i></div>
</section>

<!-- ===== OLD ROW 2 ===== -->
<section class="scr" style="left:94px;top:323px">
  <div class="hd"><span><span class="m">≡</span>Client</span><svg class="exit" viewBox="0 0 10 10"><path d="M1 1h5v8H1zM6 5h3.5M8 3.5l1.5 1.5L8 6.5" fill="none" stroke="#333"/></svg></div>
  <div class="avatar" role="img" aria-label="Client profile photo"></div>
  <div class="name">Baraka Odhiambo</div>
  <div class="info"><div><b>Activation Date</b><span>Jun 9 2024</span></div><div><b>Groups</b></div><div><b>Office</b><span>Mwangaza Branch</span></div><div><b>Mobile Number</b><span>700112233</span></div><div><b>Date of Birth</b><span>Feb 2, 1995</span></div></div>
  <div class="btn" style="justify-content:space-between;padding:0 5px;margin-top:4px">Loan Accounts<span>⌄</span></div>
</section>

<section class="scr dim" style="left:220px;top:323px">
  <div class="hd"><span><span class="m">≡</span>Client</span><span>⋮</span></div>
  <div class="info ghost" style="margin-top:56px;background:#dde6ee"><div><b>A</b></div><div><b>G</b></div><div><b>O</b></div><div><b>M</b></div><div><b>Date of Birth</b><span>Feb 2, 1995</span></div></div>
  <div class="btn" style="justify-content:space-between;padding:0 5px;margin-top:4px">Loan Accounts<span>⌄</span></div>
  <div class="menu"><span>Add Loan Account</span><span>Add Savings Account</span><span>Charges</span><span>Documents</span><span>Identifiers</span><span>More Client info</span><span>Notes</span><span>Pinpoint Location</span><span>Survey Signature</span></div>
</section>

<section class="scr" style="left:345px;top:323px">
  <div class="hd"><span><span class="m">≡</span>Client</span><svg class="exit" viewBox="0 0 10 10"><path d="M1 1h5v8H1zM6 5h3.5M8 3.5l1.5 1.5L8 6.5" fill="none" stroke="#333"/></svg></div>
  <div class="fld" style="height:12px">National ID</div><div class="fld" style="height:12px">Gender</div><div class="fld" style="height:12px">Date Of Birth</div><div class="fld" style="height:12px">Client</div><div class="fld" style="height:12px">Client Classification</div><div class="fld" style="height:12px">Office</div><div class="fld" style="height:12px">Staff</div>
  <div class="chk" style="margin-top:2px"><i></i>Client Active</div>
  <div class="btn">Submit</div>
  <div class="nav"><i></i><i class="on"></i><i></i><i></i></div>
</section>

<section class="scr" style="left:477px;top:323px">
  <div class="hd"><span><span class="m">‹</span>Loan Account Summary</span><span>⋮</span></div>
  <div style="font-size:4.2px">Baraka Odhiambo</div>
  <div class="strip"><span>● Asset Finance Loan</span><span>#000000011</span></div>
  <div><div class="kv"><span>Amount Disbursed</span><span>10000.0</span></div><div class="kv"><span>Disbursement Date</span><span>8 Jul 2024</span></div><div class="kv"><span>In Arrears</span><span>10000.0</span></div><div class="kv"><span>Staff</span><span>Odhiambo, Baraka</span></div></div>
  <table class="t-g"><thead><tr><td>Summary</td><td>Loan</td><td>Amt.Paid</td><td>Balance</td></tr></thead><tbody><tr><td>Principal</td><td>10000.0</td><td>0.0</td><td>10000.0</td></tr><tr class="hl"><td>Interest</td><td>2000.0</td><td>2000.0</td><td>0.0</td></tr><tr><td>Fees</td><td>0.0</td><td>0.0</td><td>0.0</td></tr><tr class="hl"><td>Penalty</td><td>0.0</td><td>0.0</td><td>0.0</td></tr><tr><td>Total</td><td>12000.0</td><td>2000.0</td><td>10000.0</td></tr></tbody></table>
  <div class="btn" style="margin-top:8px">Make Repayment</div>
</section>

<section class="scr" style="left:598px;top:323px">
  <div class="hd"><span><span class="m">‹</span>Loan Application</span></div>
  <div class="sel">Loan Product<i class="cv">⌄</i></div><div class="sel">Loan Purpose<i class="cv">⌄</i></div><div class="sel">Fund<i class="cv">⌄</i></div><div class="sel">Submission Date</div><div class="sel">Disbursed Date</div><div class="sel">External ID<i class="cv">⌄</i></div><div class="sel">Link Savings<i class="cv">⌄</i></div><div class="sel">Number of Repayments<i class="cv">⌄</i></div>
  <div class="split"><div class="sel">Nominal</div><span class="unit">Per Month</span><i class="ring"></i></div>
  <div class="sel">Repaid Every<i class="cv">⌄</i></div>
</section>

<section class="scr" style="left:724px;top:323px">
  <div class="hd"><span><span class="m">‹</span>Loan Application</span></div>
  <div class="sel">Link Savings<i class="cv">⌄</i></div><div class="sel">Number of Repayments<i class="cv">⌄</i></div>
  <div class="split"><div class="sel">Nominal</div><span class="unit">Per Month</span><i class="ring"></i></div>
  <div class="split"><div class="sel">Repaid Every</div><span class="unit">Term</span><i class="ring"></i></div>
  <div class="split"><div class="sel">Loan Terms</div><span class="unit">Term</span><i class="ring"></i></div>
  <div class="sel">Amortization<i class="cv">⌄</i></div><div class="sel">Interest Calculation Period<i class="cv">⌄</i></div><div class="sel">Repayment Strategy<i class="cv">⌄</i></div>
  <div class="chk" style="font-size:3.6px"><i></i>Calculate Interest for exact days in</div>
  <div class="btn">Interest Type Method</div>
</section>

<!-- ===== NEW ROW 1 ===== -->
<section class="scr" style="left:35px;top:673px">
  <div class="hd"><span><span class="m">≡</span>Client</span><svg class="exit" viewBox="0 0 10 10"><path d="M1 1h5v8H1zM6 5h3.5M8 3.5l1.5 1.5L8 6.5" fill="none" stroke="#333"/></svg></div>
  <div class="ttl">Create Client</div>
  <div class="avatar" role="img" aria-label="Client profile photo"></div>
  <div class="fld" style="height:13px">First Name</div><div class="fld" style="height:13px">Middle Name</div><div class="fld" style="height:13px">Mobile Number</div><div class="fld" style="height:13px">National ID</div><div class="fld" style="height:13px">Gender</div><div class="fld" style="height:13px">Date of Birth</div>
</section>

<section class="scr" style="left:164px;top:673px;padding-top:36px">
  <div class="brand">LoqTab</div>
  <div class="dots"><i></i><i></i><i></i><i></i><i></i><i></i></div>
  <div class="pad"><span>1</span><span>2</span><span>3</span><span>4</span><span>5</span><span>6</span><span>7</span><span>8</span><span>9</span><i></i><span>0</span><i class="del"></i></div>
  <div class="note" style="margin-top:6px">Forget Passcode Login Manually</div>
</section>

<section class="scr" style="left:295px;top:673px">
  <div class="hd"><span><span class="m">≡</span>Loan Book</span><svg class="exit" viewBox="0 0 10 10"><path d="M1 1h5v8H1zM6 5h3.5M8 3.5l1.5 1.5L8 6.5" fill="none" stroke="#333"/></svg></div>
  <div class="row" style="font-size:4.4px">Filter<span class="funnel"><svg width="6" height="6" viewBox="0 0 10 10"><path d="M1 1h8L6 5v4L4 8V5z" fill="none" stroke="#fff"/></svg></span></div>
  <div class="tabs" style="margin:4px 0 8px"><span class="tab">Loan Summary</span><span>Loan Listing</span></div>
  <div class="card n" style="padding:6px 4px;gap:5px"><div class="row"><span>Name:</span><span>Amani Kiprono</span></div><div class="row"><span>Mobile No:</span><span>7200001234</span></div><div class="row"><span>Outstanding Balance:</span><span>90000.0</span></div><div class="row"><span>Last Repayment Date:</span><span>2024-07-08</span></div><div class="row"><span>Next Repayment Date:</span><span>2024-08-08</span></div></div>
</section>

<section class="scr" style="left:425px;top:673px">
  <div class="hd"><span><span class="m">≡</span>Loan Book</span><svg class="exit" viewBox="0 0 10 10"><path d="M1 1h5v8H1zM6 5h3.5M8 3.5l1.5 1.5L8 6.5" fill="none" stroke="#333"/></svg></div>
  <div class="row" style="font-size:5px">Filter<span class="funnel"><svg width="6" height="6" viewBox="0 0 10 10"><path d="M1 1h8L6 5v4L4 8V5z" fill="none" stroke="#fff"/></svg></span></div>
  <div class="tabs"><span class="tab">Loan Summary</span><span>Loan Listing</span></div>
  <div class="tiles" style="background:var(--soft);padding:2px"><div class="tile n">0<br>Total Active Clients</div><div class="tile n">0<br>Total New Clients</div><div class="tile n">30012.00 to 3 Clients<br>Total Disbursed</div><div class="tile n">5502.00 from 3 Clients<br>Total Collected</div><div class="tile n">0.00 from 0 Clients<br>Total Missed</div></div>
  <div class="li" style="margin-top:4px"><span>Total Active<br><b>0.00 for 0 Clients</b></span><i class="ring"></i></div>
  <div class="li"><span>Total Near Due<br><b>20516.53 from 3 Clients</b></span><i class="ring"></i></div>
  <div class="li"><span>Total Due<br><b>0.00 from 0 Clients</b></span><i class="ring"></i></div>
  <div class="li"><span>Total Overdue<br><b>0.00 for 0 Clients</b></span><i class="ring"></i></div>
</section>

<section class="scr" style="left:555px;top:673px">
  <div class="hd"><span><span class="m">≡</span>Clients</span><svg class="exit" viewBox="0 0 10 10"><path d="M1 1h5v8H1zM6 5h3.5M8 3.5l1.5 1.5L8 6.5" fill="none" stroke="#333"/></svg></div>
  <div class="search" style="margin:6px 0">Search here<span>⌕</span></div>
  <div class="li cl"><span>Baraka Odhiambo<br><b>000000001</b></span><i class="ring"></i></div>
  <div class="li cl"><span>Jabali Mwende<br><b>000000002</b></span><i class="ring"></i></div>
  <div class="li cl"><span>Amani Kiprono<br><b>000000003</b></span><i class="ring"></i></div>
  <div class="li cl"><span>Zawadi Njeri<br><b>000000004</b></span><i class="ring"></i></div>
  <div class="li cl"><span>Tumaini Achieng<br><b>000000005</b></span><i class="ring"></i></div>
  <div class="li cl"><span>Faraji Oloo Wekesa<br><b>000000006</b></span><i class="ring"></i></div>
  <div class="li cl"><span>Amani Kiprono<br><b>000000007</b></span><i class="ring"></i></div>
</section>

<section class="scr" style="left:684px;top:673px">
  <div class="hd"><span><span class="m">≡</span>Client</span><svg class="exit" viewBox="0 0 10 10"><path d="M1 1h5v8H1zM6 5h3.5M8 3.5l1.5 1.5L8 6.5" fill="none" stroke="#333"/></svg></div>
  <div class="brand" style="margin-top:10px">LoqTab</div>
  <div class="ttl" style="margin:3px 0 22px">Please enter your<br>credentials</div>
  <div class="fld" style="height:13px">Tenant<span>▦</span></div><div class="fld" style="height:13px">Username<span>●</span></div><div class="fld" style="height:13px">Password<span>◉</span></div>
  <div class="btn" style="margin-top:4px;height:12px">Login</div>
</section>

<section class="scr" style="left:813px;top:673px">
  <div class="hd"><span><span class="m">≡</span>Loan Book</span><svg class="exit" viewBox="0 0 10 10"><path d="M1 1h5v8H1zM6 5h3.5M8 3.5l1.5 1.5L8 6.5" fill="none" stroke="#333"/></svg></div>
  <div class="row" style="font-size:5.5px;font-weight:500;margin-bottom:10px">Filters<span class="funnel" style="color:#fff;font-size:6px">×</span></div>
  <div class="sel" style="height:13px;margin-bottom:4px"><span>Loan Status<br><b>Select Loan Status</b></span><i class="cv">⌄</i></div>
  <div class="sel" style="height:13px;margin-bottom:4px"><span>Office<br><b>Select Offices</b></span><i class="cv">⌄</i></div>
  <div class="sel" style="height:13px;margin-bottom:4px"><span>Loan Officers<br><b>No Loan Officers Found</b></span><i class="cv">⌄</i></div>
  <div class="sel" style="height:13px;margin-bottom:4px"><span>Loan Products<br><b>Select Loan Products</b></span><i class="cv">⌄</i></div>
  <div class="sel" style="height:13px"><span>Funds<br><b>Select Funds</b></span><i class="cv">⌄</i></div>
  <div class="row" style="justify-content:center;gap:4px;margin-top:14px"><span class="btn sm">Apply filters</span><span class="btn sm">Clear filters</span></div>
</section>

<!-- ===== NEW ROW 2 ===== -->
<section class="scr" style="left:95px;top:909px">
  <div class="hd"><span><span class="m">≡</span>Client</span><svg class="exit" viewBox="0 0 10 10"><path d="M1 1h5v8H1zM6 5h3.5M8 3.5l1.5 1.5L8 6.5" fill="none" stroke="#333"/></svg></div>
  <div class="avatar" role="img" aria-label="Client profile photo"></div>
  <div class="name">Baraka Odhiambo</div>
  <div class="info" style="gap:10px"><div><b>Activation Date</b><span>Jun 9 2024</span></div><div><b>Groups</b></div><div><b>Office</b><span>Mwangaza Branch</span></div><div><b>Mobile Number</b><span>700112233</span></div><div><b>Date of Birth</b><span>Feb 2, 1995</span></div></div>
  <div class="btn" style="justify-content:space-between;padding:0 5px;margin-top:4px">Loan Accounts<span>⌄</span></div>
</section>

<section class="scr dim" style="left:224px;top:909px">
  <div class="hd"><span><span class="m">≡</span>Client</span><span>⋮</span></div>
  <div class="info ghost" style="margin-top:56px;background:#dde6ee"><div><b>A</b></div><div><b>G</b></div><div><b>O</b></div><div><b>M</b></div><div><b>Date of Birth</b><span>Feb 2, 1995</span></div></div>
  <div class="btn" style="justify-content:space-between;padding:0 5px;margin-top:4px">Loan Accounts<span>⌄</span></div>
  <div class="menu" style="gap:5px"><span>Add Loan Account</span><span>Add Savings Account</span><span>Charges</span><span>Documents</span><span>Identifiers</span><span>More Client info</span><span>Notes</span><span>Pinpoint Location</span><span>Survey Signature</span></div>
</section>

<section class="scr" style="left:352px;top:909px">
  <div class="hd"><span><span class="m">≡</span>Client</span><svg class="exit" viewBox="0 0 10 10"><path d="M1 1h5v8H1zM6 5h3.5M8 3.5l1.5 1.5L8 6.5" fill="none" stroke="#333"/></svg></div>
  <div class="fld" style="height:13px;margin-top:3px">National ID</div><div class="fld" style="height:13px">Gender</div><div class="fld" style="height:13px">Date Of Birth</div><div class="fld" style="height:13px">Client</div><div class="fld" style="height:13px">Client Classification</div><div class="fld" style="height:13px">Office</div><div class="fld" style="height:13px">Staff</div>
  <div class="chk" style="margin-top:4px"><i></i>Client Active</div>
  <div class="btn" style="height:12px">Submit</div>
</section>

<section class="scr" style="left:487px;top:909px">
  <div class="hd"><span><span class="m">‹</span>Loan Account Summary</span><span>⋮</span></div>
  <div style="font-size:4.2px">Baraka Odhiambo</div>
  <div class="strip"><span>● Asset Finance Loan</span><span>#000000011</span></div>
  <div style="background:#f3f3f3;padding:1px 2px"><div class="kv"><span>Amount Disbursed</span><span>10000.0</span></div><div class="kv"><span>Disbursement Date</span><span>8 Jul 2024</span></div><div class="kv"><span>In Arrears</span><span>10000.0</span></div><div class="kv"><span>Staff</span><span>Odhiambo, Baraka</span></div></div>
  <table class="t-n"><thead><tr><td>Summary</td><td>Loan</td><td>Amt Paid</td><td>Balance</td></tr></thead><tbody><tr><td>Principal</td><td>10000.0</td><td>0.0</td><td>10000.0</td></tr><tr class="hl"><td>Interest</td><td>2000.0</td><td>2000.0</td><td>0.0</td></tr><tr><td>Fees</td><td>0.0</td><td>0.0</td><td>0.0</td></tr><tr class="hl"><td>Penalty</td><td>0.0</td><td>0.0</td><td>0.0</td></tr><tr><td>Total</td><td>12000.0</td><td>2000.0</td><td>10000.0</td></tr></tbody></table>
  <div class="btn" style="margin-top:8px;height:12px">Make Repayment</div>
</section>

<section class="scr" style="left:612px;top:909px">
  <div class="hd"><span><span class="m">‹</span>Loan Application</span></div>
  <div class="sel" style="height:12px">Loan Product<i class="cv">⌄</i></div><div class="sel" style="height:12px">Loan Purpose<i class="cv">⌄</i></div><div class="sel" style="height:12px">Fund<i class="cv">⌄</i></div><div class="sel" style="height:12px">Submission Date</div><div class="sel" style="height:12px">Disbursed Date</div><div class="sel" style="height:12px">External ID<i class="cv">⌄</i></div><div class="sel" style="height:12px">Link Savings<i class="cv">⌄</i></div><div class="sel" style="height:12px">Number of Repayments<i class="cv">⌄</i></div>
  <div class="split"><div class="sel" style="height:12px">Nominal</div><span class="unit">Per Month</span><i class="ring"></i></div>
  <div class="sel" style="height:12px">Repaid Every<i class="cv">⌄</i></div>
</section>

<section class="scr" style="left:741px;top:909px">
  <div class="hd"><span><span class="m">‹</span>Loan Application</span></div>
  <div class="sel" style="height:12px">Link Savings<i class="cv">⌄</i></div><div class="sel" style="height:12px">Number of Repayments<i class="cv">⌄</i></div>
  <div class="split"><div class="sel" style="height:12px">Nominal</div><span class="unit">Per Month</span><i class="ring"></i></div>
  <div class="split"><div class="sel" style="height:12px">Repaid Every</div><span class="unit">Term</span><i class="ring"></i></div>
  <div class="split"><div class="sel" style="height:12px">Loan Terms</div><span class="unit">Term</span><i class="ring"></i></div>
  <div class="sel" style="height:12px">Amortization<i class="cv">⌄</i></div><div class="sel" style="height:12px">Interest Calculation Period<i class="cv">⌄</i></div><div class="sel" style="height:12px">Repayment Strategy<i class="cv">⌄</i></div>
  <div class="chk" style="font-size:3.6px"><i></i>Calculate Interest for exact days in</div>
  <div class="btn" style="height:12px">Interest Type Method</div>
</section>

</body>
</html>
```